Wadi Alsafeer
Wadi Alsafeer - Construction
Creative Brief
Simple
Salem Dabbagh
CEO
Locality 428 - Alley 17 - House 9 Al Dhaheera - Baghdad - Iraq
ceo@wadialsafeer.com
www.wadialsafeer.com
rokba72x rokba72x
i uploaded the final files so you all can work now with it and very soon I'll chose a winner
and i wont you to make these changes in the latter head only: 1- add the address in Arabic language ( محلة 428 - زقاق 17 - دار 9) and 2- change the e-mail into ( info@wadialsafeer.com ) thank you
Hello , great job all i just wont you to add the name and title in English and Arabic language in the businesses cards only, ( name in Arabic : سالم دباغ) and the title(CEO) in Arabic ( المدير المفوض) Regards,

```html
<!DOCTYPE html>
<html lang="en">
<head>
<meta charset="utf-8">
<title>Wadi Alsafeer – Business Card</title>
<link rel="stylesheet" href="https://fonts.googleapis.com/css2?family=Cairo:wght@400;600&family=Open+Sans:wght@400;600;700&display=swap">
<style>
  :root {
    --page-bg: #e9e9ea;
    --card-white: #f7f7f8;
    --brand-blue: #1f86d3;
    --brand-grey: #6b6e72;
    --text-dark: #45484c;
    --divider: #b9bcc0;
    --band-text: #ffffff;
  }
  * { margin: 0; padding: 0; box-sizing: border-box; }
  html, body { width: 1200px; height: 898px; overflow: hidden; }
  body {
    background: var(--page-bg);
    font-family: "Open Sans", sans-serif;
    position: relative;
  }
  .card {
    position: absolute;
    left: 330px;
    width: 540px;
    height: 308px;
    background: var(--card-white);
    overflow: hidden;
    box-shadow: 0 4px 14px rgba(0,0,0,0.12);
  }
  .card--front { top: 110px; }
  .card--back { top: 480px; }

  .wordmark {
    display: flex;
    align-items: center;
    gap: 10px;
    color: var(--brand-blue);
    font-weight: 700;
    letter-spacing: 0.04em;
    text-transform: uppercase;
    white-space: nowrap;
  }
  .wordmark__mark {
    width: 14px; height: 14px;
    background: var(--brand-blue);
  }
  .card--front .wordmark {
    position: absolute;
    left: 0; right: 0; top: 0; bottom: 0;
    justify-content: center;
    font-size: 34px;
  }
  .card--back .wordmark {
    position: absolute;
    left: 40px; top: 62px;
    font-size: 22px;
  }
  .card--back .wordmark__mark { width: 11px; height: 11px; }

  .contact {
    position: absolute;
    left: 300px; top: 38px;
    padding-left: 14px;
    border-left: 1px solid var(--divider);
    color: var(--text-dark);
    font-size: 11px;
    line-height: 17px;
    white-space: nowrap;
  }
  .contact__row { display: flex; align-items: center; gap: 6px; }
  .contact__icon { width: 10px; height: 10px; flex: none; }

  .swoosh { position: absolute; left: 0; top: 0; width: 540px; height: 308px; }
  .holder {
    position: absolute;
    left: 0; right: 0; bottom: 14px;
    text-align: center;
    color: var(--band-text);
    white-space: nowrap;
  }
  .holder__line {
    font-size: 12px;
    line-height: 18px;
    letter-spacing: 0.18em;
  }
  .holder__name { font-weight: 600; text-transform: uppercase; }
  .holder__line--arabic {
    font-family: "Cairo", sans-serif;
    font-size: 13px;
    line-height: 22px;
    letter-spacing: 0;
    margin-top: 2px;
  }
  .holder__line--arabic .holder__name { font-weight: 600; }
</style>
</head>
<body>

  <section class="card card--front">
    <div class="wordmark"><span class="wordmark__mark"></span>Wadi Alsafeer</div>
  </section>

  <section class="card card--back">
    <svg class="swoosh" viewBox="0 0 540 308" aria-hidden="true">
      <path d="M0 205 C 150 250, 330 215, 540 120 L540 308 L0 308 Z" fill="var(--brand-blue)"/>
      <path d="M0 188 C 170 238, 340 200, 540 98" fill="none" stroke="var(--brand-grey)" stroke-width="9"/>
    </svg>

    <div class="wordmark"><span class="wordmark__mark"></span>Wadi Alsafeer</div>

    <div class="contact">
      <div>047 9th Floor Tower</div>
      <div>Canal Road BGD</div>
      <div class="contact__row">
        <svg class="contact__icon" viewBox="0 0 10 10"><path d="M2 1 L4 1 L5 3 L4 4 Q5 6 6 6 L7 5 L9 6 L9 8 Q5 9 1 3 Z" fill="var(--brand-blue)"/></svg>
        014 227 5093
      </div>
      <div class="contact__row">
        <svg class="contact__icon" viewBox="0 0 10 10"><rect x="0.5" y="2" width="9" height="6" fill="var(--brand-blue)"/><path d="M0.5 2 L5 5.5 L9.5 2" fill="none" stroke="#fff" stroke-width="0.8"/></svg>
        hello@mailbox.com
      </div>
      <div class="contact__row">
        <svg class="contact__icon" viewBox="0 0 10 10"><circle cx="5" cy="5" r="4.5" fill="var(--brand-blue)"/><path d="M0.5 5 H9.5 M5 0.5 V9.5" stroke="#fff" stroke-width="0.7"/></svg>
        www.yoursitehere.com
      </div>
    </div>

    <div class="holder">
      <div class="holder__line"><span class="holder__name">Salem Dabbagh</span> Managing Director</div>
      <div class="holder__line holder__line--arabic" lang="ar" dir="rtl"><span class="holder__name">سالم دباغ</span> – المدير المفوض</div>
    </div>
  </section>

</body>
</html>
```